Business cards and letterhead
Business cards and letterhead - Pharmacy/Pharmaceuticals
Creative Brief
Professional
Owen Lilcroft
Partner
4178 Heron Lake Road Suite 410 Grapevine, TX 76099
owen@torvalepz.com
torvalepz.com

```html
<!DOCTYPE html>
<html lang="en">
<head>
<meta charset="utf-8">
<title>Torvale business card</title>
<link href="https://fonts.googleapis.com/css2?family=Arimo:wght@400;700&display=swap" rel="stylesheet">
<style>
  :root {
    --stage: #4a4a4b;
    --blue-deep: #0f4fa8;
    --blue-mid: #2a78cf;
    --blue-light: #6fb6ee;
    --paper: #ffffff;
    --paper-shade: #dcdde0;
    --ink: #3b3d42;
    --white: #ffffff;
  }
  html, body {
    margin: 0;
    padding: 0;
    overflow: hidden;
  }
  body {
    width: 1200px;
    height: 895px;
    background: var(--stage);
    position: relative;
    font-family: "Arimo", Arial, sans-serif;
  }
  .card {
    position: absolute;
    width: 620px;
    height: 354px;
    overflow: hidden;
    background: var(--paper);
  }
  .card svg.card-art {
    position: absolute;
    inset: 0;
    width: 620px;
    height: 354px;
  }
  .card-front { left: 60px; top: 50px; }
  .card-back { left: 520px; top: 490px; }

  .brand {
    position: absolute;
    left: 28px;
    top: 112px;
    width: 140px;
    display: flex;
    flex-direction: column;
    align-items: center;
    gap: 10px;
  }
  .brand-dot {
    width: 48px;
    height: 48px;
    border-radius: 50%;
    background: var(--blue-mid);
  }
  .brand-name {
    font-weight: 700;
    font-size: 31px;
    line-height: 1;
    color: var(--blue-deep);
    letter-spacing: -0.3px;
    white-space: nowrap;
  }

  .contact {
    position: absolute;
    right: 36px;
    top: 66px;
    color: var(--white);
    text-align: right;
  }
  .person-name {
    font-size: 17px;
    letter-spacing: 1px;
    text-transform: uppercase;
    margin: 0 24px 2px 0;
  }
  .person-role {
    font-size: 12.5px;
    margin: 0 24px 0 0;
    opacity: 0.92;
  }
  .address {
    font-size: 11.5px;
    line-height: 18px;
    margin: 30px 24px 20px 0;
  }
  .contact-list {
    list-style: none;
    margin: 0;
    padding: 0;
    font-size: 11.5px;
  }
  .contact-list li {
    display: flex;
    justify-content: flex-end;
    align-items: center;
    gap: 10px;
    height: 19px;
  }
  .contact-list li.gap { margin-bottom: 4px; }
  .contact-list svg { width: 14px; height: 14px; flex: none; }

  .website {
    position: absolute;
    right: 40px;
    top: 288px;
    font-size: 21px;
    letter-spacing: 6px;
    color: var(--ink);
  }
</style>
</head>
<body>

<section class="card card-front" aria-label="Business card front">
  <svg class="card-art" viewBox="0 0 620 354" aria-hidden="true">
    <defs>
      <linearGradient id="paperFront" x1="0" y1="0" x2="1" y2="0">
        <stop offset="0" stop-color="#f4f5f7"/>
        <stop offset="1" stop-color="#ffffff"/>
      </linearGradient>
      <radialGradient id="blueFront" cx="0.45" cy="0.2" r="0.9">
        <stop offset="0" stop-color="#4d9be6"/>
        <stop offset="0.55" stop-color="#2a78cf"/>
        <stop offset="1" stop-color="#0f4fa8"/>
      </radialGradient>
    </defs>
    <rect width="620" height="354" fill="url(#paperFront)"/>
    <path d="M262 0 C196 100 196 254 262 354 L620 354 L620 0 Z" fill="url(#blueFront)"/>
    <path d="M246 0 C178 100 178 254 246 354" fill="none" stroke="#2a78cf" stroke-width="5"/>
  </svg>

  <div class="brand">
    <span class="brand-dot"></span>
    <span class="brand-name">Torvale</span>
  </div>

  <div class="contact">
    <p class="person-name">Owen Lilcroft</p>
    <p class="person-role">Partner</p>
    <p class="address">4178 Heron Lake Road Suite 410<br>Grapevine, TX 76099</p>
    <ul class="contact-list">
      <li class="gap">012 555 0147
        <svg viewBox="0 0 14 14"><path d="M3 1 L5.5 1 L6.5 4 L5 5.2 C5.8 7 7 8.2 8.8 9 L10 7.5 L13 8.5 L13 11 C13 12 12 13 11 13 C6 12.5 1.5 8 1 3 C1 2 2 1 3 1 Z" fill="#fff"/></svg>
      </li>
      <li class="gap">012 555 0148
        <svg viewBox="0 0 14 14"><rect x="3.5" y="0.5" width="7" height="13" rx="1.2" fill="none" stroke="#fff" stroke-width="1.2"/><circle cx="7" cy="11.3" r="0.8" fill="#fff"/></svg>
      </li>
      <li class="gap">012 555 0149
        <svg viewBox="0 0 14 14"><rect x="3.5" y="1" width="7" height="4" fill="#fff"/><rect x="1" y="5" width="12" height="5" rx="1" fill="#fff"/><rect x="3.5" y="9" width="7" height="4" fill="#fff" stroke="#2a78cf" stroke-width="0.8"/></svg>
      </li>
      <li>owen@torvalepz.com
        <svg viewBox="0 0 14 14"><rect x="1" y="3" width="12" height="8.5" fill="#fff"/><path d="M1 3 L7 8 L13 3" fill="none" stroke="#2a78cf" stroke-width="1"/></svg>
      </li>
      <li>www.torvalepz.com
        <svg viewBox="0 0 14 14"><circle cx="7" cy="7" r="6" fill="none" stroke="#fff" stroke-width="1.2"/><ellipse cx="7" cy="7" rx="2.6" ry="6" fill="none" stroke="#fff" stroke-width="1"/><path d="M1 7 H13" stroke="#fff" stroke-width="1"/></svg>
      </li>
    </ul>
  </div>
</section>

<section class="card card-back" aria-label="Business card back">
  <svg class="card-art" viewBox="0 0 620 354" aria-hidden="true">
    <defs>
      <linearGradient id="paperBack" x1="0" y1="0" x2="0" y2="1">
        <stop offset="0" stop-color="#ffffff"/>
        <stop offset="1" stop-color="#dcdde0"/>
      </linearGradient>
      <radialGradient id="blueBack" cx="0.42" cy="0.3" r="0.75">
        <stop offset="0" stop-color="#8fcaf4"/>
        <stop offset="0.35" stop-color="#4d9be6"/>
        <stop offset="1" stop-color="#0f4fa8"/>
      </radialGradient>
    </defs>
    <rect width="620" height="354" fill="url(#paperBack)"/>
    <path d="M0 0 H620 V192 Q310 262 0 180 Z" fill="#6fb6ee"/>
    <path d="M0 0 H620 V176 Q310 250 0 166 Z" fill="url(#blueBack)"/>
  </svg>
  <div class="website">www.torvalepz.com</div>
</section>

</body>
</html>
```